Flyer Design Project - law firm

I need a design for an advertising flyer for my law firm.
Ideally the size of the document will be one page A4.
I have attached a copy of the logo. I would like the lettering for 'Dornwick Legal' to be all the same size, rather than the 'S' and 'L' being slightly larger
The flyer must include the text below:
Wills
Anyone who owns property or investments or has family obligations should have a Will to ensure that their assets are distributed in accordance with their wishes and that their children are cared for by the guardians of their choosing. Without a Will, these vital decisions are determined by the government or the courts of the State or Territory which you lived in at the time of your death.
Dornwick Legal can assist you in the preparation of a legal will tailored to your particular circumstances to ensure that your wishes are followed.
We are offering Halbrook- Crestmere clients a free discussion of their will requirements and a heavily discounted standard wills package of
$330.00* for a single will
$550.00* for couples wills
These prices are only valid prior to your conveyancing settlement for standard wills (e.g. not including a testamentary trust or other complications.
Please contact us on or provide Halbrook Crestmere with authority for us to contact you today.
Updates
Hi All,
I have posted a copy of the proposed logo. Please note that I need the wording of 'Dornwick Legal' to all be the same size, rather than the 'S' and 'L' being slightly larger.
If you require anything further please let me know.
Thanks
I have added copies of the logo in ups format,
If you require anything further please let know.
Thanks for your assistance.
Industry/Entity Type
Advertising
Look and feel
Each slider illustrates characteristics of the customer's brand and the style your logo design should communicate.

```html
<!DOCTYPE html>
<html lang="en">
<head>
<meta charset="utf-8">
<title>Dornwick Legal – Wills</title>
<link href="https://fonts.googleapis.com/css2?family=Cinzel:wght@400&family=Great+Vibes&family=Open+Sans:wght@400&display=swap" rel="stylesheet">
<style>
  :root {
    --black: #000000;
    --orange: #f26a1b;
    --orange-deep: #ff4a12;
    --orange-light: #ff9a2a;
    --text: #1d1d1d;
    --paper: #ffffff;
    --paper-shade: #ececec;
    --white: #ffffff;
  }
  * { margin: 0; padding: 0; box-sizing: border-box; }
  html, body { width: 849px; height: 1200px; overflow: hidden; background: var(--paper); }
  .flyer {
    position: relative;
    width: 849px;
    height: 1200px;
    overflow: hidden;
    font-family: Arial, Helvetica, sans-serif;
    color: var(--text);
    background: radial-gradient(ellipse at 55% 45%, var(--paper) 35%, var(--paper-shade) 100%);
  }
  .masthead {
    position: absolute;
    left: 0; top: 0;
    width: 849px; height: 371px;
    background: var(--black);
  }
  .masthead-stripe {
    position: absolute;
    left: 342px; top: 63px;
    width: 507px; height: 15px;
    background: linear-gradient(90deg, rgba(242,106,27,0) 0%, #6b3a1c 25%, var(--orange) 100%);
  }
  .gavel-art {
    position: absolute;
    left: 662px; top: 112px;
    width: 187px; height: 213px;
    background: radial-gradient(ellipse at 55% 45%, #7a4a2c 0%, #3a2417 55%, #000000 100%);
  }
  .brand {
    position: absolute;
    left: 111px; top: 137px;
    display: flex;
    align-items: center;
    gap: 20px;
    z-index: 1;
  }
  .brand-dot {
    width: 112px; height: 112px;
    border-radius: 50%;
    background: var(--orange);
  }
  .brand-name {
    font-family: "Cinzel", Georgia, serif;
    font-size: 38px;
    font-weight: 400;
    color: var(--white);
    text-transform: uppercase;
    white-space: nowrap;
  }
  .title-script {
    position: absolute;
    left: 100px; top: 410px;
    font-family: "Great Vibes", cursive;
    font-size: 96px;
    font-weight: 400;
    line-height: 1;
    color: var(--orange);
  }
  .content {
    position: absolute;
    left: 341px; top: 452px;
    width: 373px;
    font-size: 15.4px;
    line-height: 18.8px;
  }
  .content p { text-align: justify; }
  .content strong { font-weight: 700; }
  .lead + .lead { margin-top: 20px; }
  .offer-heading {
    margin-top: 36px;
    font-size: 27px;
    line-height: 28px;
    font-weight: 700;
    color: var(--orange);
  }
  .price {
    margin-top: 16px;
    font-size: 16px;
    line-height: 32px;
  }
  .price b { font-size: 30px; font-weight: 700; }
  .price + .price { margin-top: 12px; }
  .terms { margin-top: 24px; letter-spacing: 0.3px; }
  .footer-wave { position: absolute; left: 0; top: 930px; }
  .contact {
    position: absolute;
    left: 485px; top: 1113px;
    list-style: none;
    font-family: "Open Sans", Arial, sans-serif;
    font-size: 16px;
    color: var(--white);
  }
  .contact li { display: flex; align-items: center; gap: 10px; height: 26px; }
  .contact svg { width: 13px; height: 13px; }
</style>
</head>
<body>
<main class="flyer">
  <header class="masthead">
    <div class="masthead-stripe"></div>
    <div class="gavel-art" role="img" aria-label="Wooden judge's gavel with gold band resting on a sound block"></div>
    <div class="brand">
      <span class="brand-dot"></span>
      <span class="brand-name">Dornwick Legal</span>
    </div>
  </header>

  <h1 class="title-script">Wills</h1>

  <section class="content">
    <p class="lead">Anyone who owns property or investments or has family obligations should have a Will to ensure that their assets are distributed in accordance with their wishes and that their children are cared for by the guardians of their choosing. Without a Will, these vital decisions are determined by the government or the courts of the State or Territory which you lived in at the time of your death.</p>
    <p class="lead"><strong>Dornwick Legal</strong> can assist you in the preparation of a legal will tailored to your particular circumstances to ensure that your wishes are followed.</p>
    <h2 class="offer-heading">Free Discussion</h2>
    <p>We are offering Halbrook- Crestmere clients a free discussion of their will requirements and a heavily discounted standard wills package of</p>
    <div class="price"><b>$330.00*</b> for a single will</div>
    <div class="price"><b>$550.00*</b> for couples wills.</div>
    <p class="terms">These prices are only valid prior to your conveyancing settlement for standard wills (e.g. not including a testamentary trust or other complications).</p>
  </section>

  <svg class="footer-wave" width="849" height="270" viewBox="0 0 849 270" aria-hidden="true">
    <defs>
      <linearGradient id="footerOrange" x1="0" y1="0" x2="1" y2="0">
        <stop offset="0" stop-color="#ff9a2a"/>
        <stop offset="0.55" stop-color="#f26a1b"/>
        <stop offset="1" stop-color="#ff4a12"/>
      </linearGradient>
      <linearGradient id="footerShade" x1="0" y1="0" x2="1" y2="0">
        <stop offset="0" stop-color="#d8d8d8" stop-opacity="0.2"/>
        <stop offset="1" stop-color="#bdbdbd"/>
      </linearGradient>
    </defs>
    <path d="M0 180 C 300 150, 600 110, 849 45 L 849 90 C 600 140, 300 175, 0 200 Z" fill="url(#footerShade)"/>
    <path d="M0 195 C 300 170, 600 135, 849 60 L 849 270 L 0 270 Z" fill="var(--paper)"/>
    <path d="M0 211 C 300 190, 600 150, 849 88 L 849 270 L 0 270 Z" fill="url(#footerOrange)"/>
  </svg>

  <ul class="contact">
    <li>
      <svg viewBox="0 0 13 13" aria-hidden="true"><rect width="13" height="13" rx="3" fill="#fff"/><path d="M3 5 h7 v1.4 h-1.5 v-0.6 h-4 v0.6 H3 Z M4.5 7 h4 l0.8 3 h-5.6 Z" fill="#f26a1b"/></svg>
      <span>98-5120-3377</span>
    </li>
    <li>
      <svg viewBox="0 0 13 13" aria-hidden="true"><rect width="13" height="13" rx="3" fill="#fff"/><rect x="2.5" y="5" width="8" height="3" fill="#f26a1b"/></svg>
      <span>www.dornwicklegal.com</span>
    </li>
  </ul>
</main>
</body>
</html>
```